brikMOSA corporation pty ltd

Contruction industry
It's a wall and floor tiling business

Industry/Entity Type

Business

Requirements
Must have
• Likes-
- clean and easy to read
- a witty design is always well received
- for it to look reputable in the industry
- a strong and direct presentation
- simple but striking colour selection
Should not have
• Dislikes-
- pls no tacky square tiles to resemble tiling

```html
<!DOCTYPE html>
<html lang="en">
<head>
<meta charset="utf-8">
<title>brikMOSA corporation pty ltd — Business Card</title>
<link rel="stylesheet" href="https://fonts.googleapis.com/css2?family=Share+Tech&display=swap">
<style>
  :root {
    --card-bg: #353431;
    --ink: #ffffff;
  }
  html, body {
    margin: 0;
    padding: 0;
    width: 750px;
    height: 1200px;
    overflow: hidden;
    background: var(--card-bg);
  }
  .card {
    position: relative;
    width: 750px;
    height: 1200px;
    background: var(--card-bg);
    color: var(--ink);
    font-family: "Share Tech", sans-serif;
  }
  .brand {
    position: absolute;
    top: 78px;
    right: 68px;
    text-align: right;
  }
  .brand-name {
    margin: 0;
    font-size: 100px;
    font-weight: 400;
    line-height: 1;
    letter-spacing: 6px;
  }
  .brand-tagline {
    margin: 22px 0 0;
    font-size: 18px;
    letter-spacing: 7.5px;
    text-transform: uppercase;
    line-height: 1;
  }
  .contact {
    position: absolute;
    right: 55px;
    text-align: right;
    margin: 0;
    line-height: 1;
  }
  .person-name {
    top: 728px;
    font-size: 54px;
    font-variant: small-caps;
    letter-spacing: 3px;
    font-weight: 400;
  }
  .person-role {
    top: 796px;
    font-size: 38px;
    font-variant: small-caps;
    letter-spacing: 2px;
  }
  .phone {
    top: 938px;
    font-size: 40px;
    letter-spacing: 1px;
  }
  .email {
    top: 1086px;
    font-size: 33px;
    letter-spacing: 6px;
    text-transform: uppercase;
  }
</style>
</head>
<body>
  <main class="card">
    <header class="brand">
      <h1 class="brand-name">brikMOSA</h1>
      <p class="brand-tagline">corporation pty ltd</p>
    </header>
    <h2 class="contact person-name">Dan Marek</h2>
    <p class="contact person-role">Director</p>
    <p class="contact phone">0400 118 352</p>
    <p class="contact email">dan.marek@example.com</p>
  </main>
</body>
</html>
```